We need a business card design for a Dubai based company .

We need a business card for a Dubai based company called "Marwaneq Smoking Requisites Trading LLC". We mainly import Flavoured Tobacco products and Charcoal which is used for smoking in a Hookah/Shisha and distribute to the wholesalers and retailers. Logo file is attached herewith.

```html
<!DOCTYPE html>
<html lang="en">
<head>
<meta charset="utf-8">
<title>Marwaneq Business Card</title>
<link rel="stylesheet" href="https://fonts.googleapis.com/css2?family=Exo+2:wght@400;600;700&display=swap">
<style>
  :root {
    --brand-red: #bb3f43;
    --ink: #1f1f1f;
    --paper: #f7f7f7;
    --backdrop: #dcdcdc;
    --rule: #9a9a9a;
  }
  * { box-sizing: border-box; margin: 0; padding: 0; }
  html, body { width: 1200px; height: 930px; overflow: hidden; }
  body {
    background: var(--backdrop);
    font-family: "Exo 2", sans-serif;
    display: flex;
    flex-direction: column;
    align-items: center;
    justify-content: center;
    gap: 44px;
  }
  .card {
    width: 700px;
    height: 400px;
    position: relative;
    box-shadow: 0 8px 24px rgba(0,0,0,0.12);
  }
  .card--front { background: var(--paper); color: var(--ink); }
  .card--back { background: var(--brand-red); color: #fff; display: flex; align-items: center; justify-content: center; }

  .wordmark { display: flex; flex-direction: column; align-items: center; }
  .wordmark__row { display: flex; align-items: center; gap: 16px; }
  .wordmark__square { width: 18px; height: 18px; background: currentColor; }
  .wordmark__name {
    font-weight: 400;
    letter-spacing: 12px;
    font-size: 46px;
    line-height: 1;
  }
  .wordmark__tagline {
    margin-top: 10px;
    font-size: 12px;
    letter-spacing: 5px;
    text-transform: uppercase;
  }
  .card--front .wordmark { position: absolute; top: 58px; left: 0; right: 0; }
  .card--front .wordmark__name { color: var(--ink); }
  .card--front .wordmark__square { background: var(--brand-red); }
  .card--front .wordmark__tagline { color: var(--brand-red); }

  .details {
    position: absolute;
    left: 0; right: 0; top: 200px;
    display: flex;
    justify-content: center;
    gap: 26px;
  }
  .address {
    text-align: right;
    font-size: 17px;
    line-height: 1.3;
    padding-top: 58px;
  }
  .divider { width: 1px; background: var(--rule); margin-top: 58px; height: 80px; }
  .person__name { font-weight: 700; font-size: 22px; letter-spacing: 1px; text-transform: uppercase; }
  .person__role { color: var(--brand-red); font-size: 16px; text-transform: uppercase; margin-bottom: 10px; }
  .contact { list-style: none; font-size: 17px; line-height: 1.5; }
  .contact li { display: flex; align-items: center; gap: 8px; }
  .contact svg { width: 15px; height: 15px; fill: var(--brand-red); flex: none; }
</style>
</head>
<body>
  <section class="card card--front">
    <div class="wordmark">
      <div class="wordmark__row">
        <span class="wordmark__square"></span>
        <span class="wordmark__name">MARWANEQ</span>
      </div>
      <span class="wordmark__tagline">Smoking Requisites Trading LLC</span>
    </div>
    <div class="details">
      <p class="address">421, Address line<br>goes here<br>45452,Country Name</p>
      <span class="divider"></span>
      <div class="person">
        <h1 class="person__name">Daniel Reyes</h1>
        <p class="person__role">Managing Director</p>
        <ul class="contact">
          <li><svg viewBox="0 0 24 24"><path d="M6.6 10.8a15 15 0 0 0 6.6 6.6l2.2-2.2a1 1 0 0 1 1-.25 11.4 11.4 0 0 0 3.6.57 1 1 0 0 1 1 1V20a1 1 0 0 1-1 1A17 17 0 0 1 3 4a1 1 0 0 1 1-1h3.5a1 1 0 0 1 1 1c0 1.25.2 2.45.57 3.57a1 1 0 0 1-.25 1z"/></svg>044-987 654 321</li>
          <li><svg viewBox="0 0 24 24"><path d="M2 5h20v14H2zm2 2v.5l8 5 8-5V7l-8 5z"/></svg>info@marwaneq.ae</li>
          <li><svg viewBox="0 0 24 24"><circle cx="12" cy="12" r="10"/></svg>www.marwaneq.ae</li>
        </ul>
      </div>
    </div>
  </section>

  <section class="card card--back">
    <div class="wordmark">
      <div class="wordmark__row">
        <span class="wordmark__square"></span>
        <span class="wordmark__name">MARWANEQ</span>
      </div>
      <span class="wordmark__tagline">Smoking Requisites Trading LLC</span>
    </div>
  </section>
</body>
</html>
```